Business Card Design Project 4 Construction Business

I am after a creative, but sleek and simple/ clean business card design. This design will form the basis of future items and might include a logo or simply a creative way to lay out the text of my company name 'kestrel ventures'
I like the simplicity of black and white however I would also be happy to see a splash of colour introduced somehow to give the text some interest and make it stand out.
I would like a double sided card.
I am young (ish!) and professional, offering construction and project management services, what I don't want is the traditional builders type card featuring a cheesy hammer/ saw image etc.
As the company name, kestrel ventures, suggests, we focus on working closely and collaboratively together, in synergy with all stakeholders involved in the projects that we undertake
Construction

```html
<!DOCTYPE html>
<html lang="en">
<head>
<meta charset="utf-8">
<title>Kestrel Ventures – Business Card</title>
<link href="https://fonts.googleapis.com/css2?family=Michroma&family=Questrial&display=swap" rel="stylesheet">
<style>
  :root {
    --page: #e9e9e7;
    --paper: #ffffff;
    --ink: #161616;
    --band-dark: #0d0d0d;
    --band-mid: #3a3a3a;
    --band-light: #8a8a8a;
    --reverse: #f2f2f2;
    --muted: #b9b9b9;
  }
  html, body {
    margin: 0;
    padding: 0;
    overflow: hidden;
  }
  .canvas {
    width: 1200px;
    height: 741px;
    background: var(--page);
    position: relative;
    overflow: hidden;
  }
  .card {
    position: absolute;
    top: 216px;
    width: 540px;
    height: 309px;
    background: var(--paper);
    box-shadow: 0 10px 28px rgba(0,0,0,0.18);
    overflow: hidden;
  }
  .card--front { left: 40px; }
  .card--back { left: 620px; }

  /* front */
  .front-band {
    position: absolute;
    left: 0; right: 0; bottom: 0;
    height: 132px;
    background: linear-gradient(180deg, var(--band-mid) 0%, var(--band-dark) 45%, var(--band-dark) 100%);
  }
  .front-web {
    position: absolute;
    right: 22px;
    top: 184px;
    font-family: "Questrial", sans-serif;
    font-size: 9px;
    letter-spacing: 1px;
    color: var(--muted);
  }
  .wordmark {
    position: absolute;
    display: flex;
    align-items: center;
    gap: 12px;
    color: var(--ink);
    font-family: "Michroma", sans-serif;
  }
  .wordmark__square {
    width: 20px;
    height: 20px;
    background: var(--ink);
    flex: none;
  }
  .wordmark__text {
    display: flex;
    flex-direction: column;
    line-height: 1;
  }
  .wordmark__top { font-size: 32px; letter-spacing: 2px; }
  .wordmark__bottom { font-size: 12px; letter-spacing: 11px; margin-top: 6px; }
  .card--front .wordmark { left: 140px; top: 86px; }

  /* back */
  .card--back .wordmark { left: 26px; top: 74px; }
  .card--back .wordmark__top { font-size: 26px; }
  .card--back .wordmark__bottom { font-size: 10px; letter-spacing: 9px; }
  .back-web {
    position: absolute;
    right: 18px;
    top: 20px;
    font-family: "Questrial", sans-serif;
    font-size: 9px;
    letter-spacing: 1px;
    color: #777;
  }
  .person {
    position: absolute;
    left: 26px;
    top: 150px;
    font-family: "Michroma", sans-serif;
    color: var(--ink);
  }
  .person__name {
    display: flex;
    align-items: stretch;
    font-size: 17px;
    letter-spacing: 1px;
  }
  .person__first {
    background: var(--ink);
    color: var(--paper);
    padding: 3px 6px 2px 6px;
  }
  .person__last { padding: 3px 6px 2px 6px; }
  .person__role {
    font-family: "Questrial", sans-serif;
    font-size: 13px;
    letter-spacing: 1px;
    margin: 5px 0 0 6px;
  }
  .back-band {
    position: absolute;
    left: 0; right: 0; bottom: 0;
    height: 98px;
    background: linear-gradient(90deg, var(--band-light) 0%, var(--band-mid) 30%, var(--band-dark) 60%);
  }
  .contacts {
    position: absolute;
    left: 22px;
    bottom: 14px;
    margin: 0;
    padding: 0;
    list-style: none;
    font-family: "Questrial", sans-serif;
    color: var(--reverse);
  }
  .contacts li {
    display: flex;
    align-items: center;
    gap: 8px;
    margin-top: 5px;
    font-size: 11px;
    letter-spacing: 0.5px;
  }
  .contacts li.contacts__phone { font-size: 15px; }
  .contacts svg { width: 12px; height: 12px; flex: none; }
</style>
</head>
<body>
<div class="canvas">

  <section class="card card--front" aria-label="Card front">
    <div class="wordmark">
      <span class="wordmark__square"></span>
      <span class="wordmark__text">
        <span class="wordmark__top">KESTREL</span>
        <span class="wordmark__bottom">VENTURES</span>
      </span>
    </div>
    <div class="front-band"></div>
    <div class="front-web">www.kestrelventures.com.au</div>
  </section>

  <section class="card card--back" aria-label="Card back">
    <div class="back-web">www.kestrelventures.com.au</div>
    <div class="wordmark">
      <span class="wordmark__square"></span>
      <span class="wordmark__text">
        <span class="wordmark__top">KESTREL</span>
        <span class="wordmark__bottom">VENTURES</span>
      </span>
    </div>
    <div class="person">
      <div class="person__name">
        <span class="person__first">LIAM</span>
        <span class="person__last">HARTWELL</span>
      </div>
      <div class="person__role">Director</div>
    </div>
    <div class="back-band"></div>
    <ul class="contacts">
      <li class="contacts__phone">
        <svg viewBox="0 0 12 12" aria-hidden="true"><path d="M2 1h2.5l1 2.5-1.5 1a6 6 0 0 0 3.5 3.5l1-1.5 2.5 1V11C5 11 1 7 1 2z" fill="#f2f2f2"/></svg>
        0400 555 017
      </li>
      <li>
        <svg viewBox="0 0 12 12" aria-hidden="true"><rect x="1" y="2.5" width="10" height="7" fill="none" stroke="#f2f2f2"/><path d="M1 2.5l5 4 5-4" fill="none" stroke="#f2f2f2"/></svg>
        liam@kestrelventures.com.au
      </li>
      <li>
        <svg viewBox="0 0 12 12" aria-hidden="true"><path d="M1.5 6L6 1.5 10.5 6M3 5v5.5h6V5" fill="none" stroke="#f2f2f2"/></svg>
        12 Ridgeway Ave Eastwood NSW 2122
      </li>
    </ul>
  </section>

</div>
</body>
</html>
```